TDM accounting firm Canada - Modern and professional business cards

To use our existing logo and create a modern looking business card.
We are looking for double sided style.
Silver-metallic background - our logo in front (reverse side)
The reverse side from the attachment- big logo over silver-metallic background is preferred.
we would like to have a business card template that can be modified to change names, addresses, and other

Industry/Entity Type

Accounting

Contact Information for Business Card

Reverse side silver-metallic finish

Font styles to use
Sans Serif

Requirements
Must have
• Reverse side silver-metallic finish
• Modern look

```html
<!DOCTYPE html>
<html lang="en">
<head>
<meta charset="utf-8">
<title>TDM Business Card – Front and Reverse</title>
<link rel="stylesheet" href="https://fonts.googleapis.com/css2?family=Open+Sans:wght@400;600;700&display=swap">
<style>
  :root {
    --page-bg: #e6e7e9;
    --silver-light: #f4f5f6;
    --silver-mid: #dcdee1;
    --silver-dark: #c4c7cb;
    --brand-blue: #1565b8;
    --text-blue: #1a5fae;
    --shadow: rgba(0, 0, 0, 0.18);
  }
  * { box-sizing: border-box; margin: 0; padding: 0; }
  html, body {
    width: 1200px; height: 873px; overflow: hidden;
    background: var(--page-bg);
    font-family: "Open Sans", Arial, sans-serif;
  }
  .sheet {
    width: 1200px; height: 873px;
    display: flex; align-items: center; justify-content: center; gap: 60px;
  }
  .card {
    position: relative;
    width: 525px; height: 300px;
    border-radius: 4px;
    overflow: hidden;
    box-shadow: 0 10px 24px var(--shadow);
    background:
      radial-gradient(ellipse 55% 90% at 62% 40%, rgba(255,255,255,0.55), rgba(255,255,255,0) 70%),
      repeating-linear-gradient(90deg, rgba(255,255,255,0.18) 0 1px, rgba(0,0,0,0.025) 1px 3px),
      linear-gradient(160deg, var(--silver-light) 0%, var(--silver-mid) 55%, var(--silver-dark) 100%);
  }

  .firm-name {
    font-weight: 700; color: var(--brand-blue);
    line-height: 1;
  }

  /* Front */
  .front .firm-name {
    position: absolute; left: 34px; top: 36px;
    font-size: 30px; letter-spacing: 1px;
  }
  .identity {
    position: absolute; right: 34px; top: 34px; text-align: right;
    color: var(--text-blue);
  }
  .identity-name { font-weight: 700; font-size: 22px; letter-spacing: 0.5px; text-transform: uppercase; }
  .identity-credentials { font-weight: 400; font-size: 20px; margin-top: 2px; }
  .identity-role {
    font-weight: 600; font-size: 8px; letter-spacing: 1.6px;
    text-transform: uppercase; margin-top: 8px;
  }
  .divider {
    position: absolute; left: 34px; right: 34px; top: 146px;
    height: 3px; background: var(--brand-blue);
  }
  .contacts {
    position: absolute; left: 34px; top: 164px;
    list-style: none; color: var(--text-blue);
  }
  .contact {
    display: flex; align-items: center; gap: 12px;
    font-weight: 600; font-size: 16px; line-height: 1; margin-bottom: 10px;
  }
  .contact svg { width: 18px; height: 18px; flex: none; }

  /* Reverse */
  .reverse {
    display: flex; align-items: center; justify-content: center;
  }
  .reverse .firm-name { font-size: 96px; letter-spacing: 4px; }
</style>
</head>
<body>
<main class="sheet">

  <section class="card front" aria-label="Business card front">
    <div class="firm-name">TDM</div>

    <div class="identity">
      <div class="identity-name">Marco Delgado</div>
      <div class="identity-credentials">CPA, CGA</div>
      <div class="identity-role">Principal and Senior Consultant</div>
    </div>

    <div class="divider"></div>

    <ul class="contacts">
      <li class="contact">
        <svg viewBox="0 0 18 18" aria-hidden="true"><rect width="18" height="18" rx="2" fill="var(--brand-blue)"/><rect x="6" y="3" width="6" height="12" rx="1" fill="none" stroke="#fff" stroke-width="1.4"/></svg>
        (780) 555-0142
      </li>
      <li class="contact">
        <svg viewBox="0 0 18 18" aria-hidden="true"><rect width="18" height="18" rx="2" fill="var(--brand-blue)"/><path d="M5 4c1 0 2 2 2 3s-1 1-1 1c1 2 2 3 4 4 0 0 0-1 1-1s3 1 3 2-1 2-2 2C8 15 3 10 3 6c0-1 1-2 2-2z" fill="#fff"/></svg>
        (780) 555-0187
      </li>
      <li class="contact">
        <svg viewBox="0 0 18 18" aria-hidden="true"><rect width="18" height="18" rx="2" fill="var(--brand-blue)"/><rect x="3.5" y="5" width="11" height="8" fill="none" stroke="#fff" stroke-width="1.3"/><path d="M3.5 5l5.5 4.5L14.5 5" fill="none" stroke="#fff" stroke-width="1.3"/></svg>
        marco@tdm-cpa.com
      </li>
      <li class="contact">
        <svg viewBox="0 0 18 18" aria-hidden="true"><rect width="18" height="18" rx="2" fill="var(--brand-blue)"/><circle cx="9" cy="9" r="5.5" fill="none" stroke="#fff" stroke-width="1.2"/><ellipse cx="9" cy="9" rx="2.4" ry="5.5" fill="none" stroke="#fff" stroke-width="1.1"/><path d="M3.5 9h11" stroke="#fff" stroke-width="1.1"/></svg>
        www.tdm-cpa.com
      </li>
    </ul>
  </section>

  <section class="card reverse" aria-label="Business card reverse">
    <div class="firm-name">TDM</div>
  </section>

</main>
</body>
</html>
```